Premium Personal Brand — Facebook Banner (Used Across All Platforms)

Update — Additional Color Direction
In addition to the dark charcoal/slate direction already described, I'm also interested in seeing variants with:
Dark navy blue — Deep, authoritative, intelligence-community feel. Same textured/matte treatment, not flat or bright.
Warm charcoal with steel blue accent — Keep the dark base but introduce a subtle steel blue gradient, accent line, or tonal shift. Sophisticated, modern, adds dimension without adding color noise.
Both should maintain the same premium, restrained, architectural feel described in the original brief. No bright blues, no corporate PowerPoint energy — think midnight, think depth, think weight.
Everything else in the brief remains the same.
I am building a premium personal brand as an executive advisor to founders ($5M+ revenue).
This contest is Facebook-banner–focused, but the design must represent a visual system that will be reused across:
- LinkedIn
- YouTube
I- nstagram
- X (Twitter)
- Website hero sections and other brand touchpoints
Think of the Facebook banner as the primary expression of the brand — not a one-off graphic.
This project is about discovering a high-end visual style and brand feel, not decoration.
What to design
Please submit one cohesive visual system, shown primarily as:
- Facebook banner (primary focus)
The same design language should clearly translate to all platforms listed above.
Designers are responsible for using the current recommended dimensions for each platform.
Quick clarification on background direction:
Backgrounds should have depth and texture, not flat color fields. Avoid pure white, light grey, or solid black backgrounds. Think matte, architectural materials — stone, graphite, concrete, steel — not blank canvases. Subtle tonal variation is encouraged. Obvious gradients or decorative patterns are not.
Text to use
Primary Headline:
- Your Business Is Too Valuable To Be Run On Hope.
Subheadline:
- You didn’t build a business to become its prisoner.
Name:
Paul Whitaker
The headline should be the dominant visual element.
Logo note (important)
My personal logo is currently being finalized.
For this contest:
- Use a simple “PW” monogram placeholder
- Clean, bold, geometric sans-serif
- Do not design a logo
- The winning design must allow an easy logo swap later.
Headshot note (important)
- Please do not include a headshot in the banner design.
- Most platforms display a circular profile image separately.
- The banner should stand on its own using typography, layout, and tone only.
- Design the banner assuming the profile photo will sit nearby, not inside the banner.
Style direction
The design should feel:
- Premium
- Calm
- Confident
- Restrained
- High-trust
- Dark, neutral backgrounds are preferred.
- Fewer elements are better than more.
Think:
- Owner-level advisor
- Private equity / boardroom tone
- Industrial, Modern, Minimalist, Elite, Architectural, not decorative
What to avoid
Please do not submit designs that feel:
- Promotional, hype-driven, or salesy
- Like a coach, guru, or agency
- Bright, colorful, or gradient-heavy
- Busy or over-designed
- Based on stock photos
- No motivational speaker energy.
Reaction test
- If someone sees this banner on Facebook (or later on LinkedIn, YouTube, etc.), the reaction should be:
“That person is serious. I’d trust them with important decisions.”
Final note
- I am not looking for many variations.
- I am looking for one strong visual direction you believe in.
Simple beats clever.
- Restraint beats decoration.

```html
<!DOCTYPE html>
<html lang="en">
<head>
<meta charset="UTF-8">
<title>Paul Whitaker — Banner</title>
<link rel="stylesheet" href="https://fonts.googleapis.com/css2?family=Inter+Tight:wght@800&family=Montserrat:wght@400;500&display=swap">
<style>
  :root {
    --page: #ffffff;
    --ink: #030304;
    --text: #ffffff;
    --accent: #d8c400;
    --glow-amber: rgba(120, 60, 10, 0.45);
    --glow-wine: rgba(90, 20, 40, 0.35);
    --glow-olive: rgba(80, 70, 10, 0.30);
  }
  html, body {
    margin: 0;
    width: 1200px;
    height: 1200px;
    overflow: hidden;
    background: var(--page);
  }
  .banner {
    position: absolute;
    left: 105px;
    top: 414px;
    width: 998px;
    height: 380px;
    background: var(--ink);
    overflow: hidden;
  }
  .banner__texture {
    position: absolute;
    inset: 0;
    background:
      radial-gradient(ellipse 45% 40% at 72% 88%, var(--glow-amber), transparent 70%),
      radial-gradient(ellipse 35% 30% at 95% 70%, var(--glow-olive), transparent 70%),
      radial-gradient(ellipse 40% 25% at 40% 85%, var(--glow-wine), transparent 70%),
      radial-gradient(ellipse 20% 35% at 88% 10%, rgba(70, 45, 10, 0.25), transparent 70%);
  }
  .monogram {
    position: absolute;
    left: 29px;
    top: 29px;
    width: 43px;
    height: 43px;
    border: 1.5px solid var(--accent);
    display: flex;
    align-items: center;
    justify-content: center;
    font-family: "Montserrat", sans-serif;
    font-weight: 400;
    font-size: 24px;
    color: var(--text);
    letter-spacing: -0.5px;
  }
  .message {
    position: absolute;
    left: 137px;
    top: 104px;
    color: var(--text);
  }
  .message__headline {
    margin: 0;
    font-family: "Inter Tight", sans-serif;
    font-weight: 800;
    font-size: 57px;
    line-height: 67px;
    letter-spacing: -1.2px;
    white-space: nowrap;
  }
  .message__subhead {
    margin: 6px 0 0;
    font-family: "Montserrat", sans-serif;
    font-weight: 400;
    font-size: 23.5px;
    line-height: 30px;
    white-space: nowrap;
  }
  .message__rule {
    width: 146px;
    height: 2px;
    margin-top: 11px;
    background: var(--accent);
  }
  .message__name {
    margin: 12px 0 0;
    font-family: "Montserrat", sans-serif;
    font-weight: 500;
    font-size: 16px;
    line-height: 20px;
  }
</style>
</head>
<body>
  <section class="banner">
    <div class="banner__texture" role="img" aria-label="Soft abstract waves of amber, wine and olive light flowing across a dark background"></div>
    <div class="monogram">PW</div>
    <div class="message">
      <h1 class="message__headline">Your Business Is Too Valuable<br>To Be Run On Hope.</h1>
      <p class="message__subhead">You didn’t build a business to become its prisoner.</p>
      <div class="message__rule"></div>
      <p class="message__name">Paul Whitaker</p>
    </div>
  </section>
</body>
</html>
```